Technical Assistance Flyer

We would like to update our Technical Assistance flyer. We are a wholesale distributor of specialized plumbing repair parts. We sell repair parts for backflow preventers, which are water safety valves used to protect the public drinking water system. Our core clientele is plumbing, fire sprinkler, and mechanical contractors. We are looking for a flyer to promote the technical assistance we offer to our customers. We want to be known as the leading source for backflow repair information and technical assistance. We offer free technical assistance over the phone with our toll-free 800 number, as well as our website, which has repair videos as well as step-by-step repair procedures to help the contractor complete their job quicker and more efficiently. This type of technical information and assistance is what makes us stand out from our competitors, and we want to highlight that and let prospective new customers know what makes us different and better than their current supplier. Our website has a lot of information about us, as well as examples of the repair videos and step-by-step repair procedures we would like to highlight on the flyer. Our website is www.valvemendsupply.com. I have included our current flyer and a high-resolution copy of our logo. We’d like to include some of the brand logos that we can help with, and we would like it to be more modern and less wordy than our previous flyer.

```html
<!DOCTYPE html>
<html lang="en">
<head>
<meta charset="utf-8">
<title>Backflow Repair Knowledge – Technical Assistance</title>
<link rel="stylesheet" href="https://fonts.googleapis.com/css2?family=Cabin:wght@500;600;700&display=swap">
<style>
  :root {
    --navy: #12335e;
    --navy-deep: #0f3566;
    --ink: #1d3557;
    --sky-top: #eef5fb;
    --sky-mid: #dbe9f5;
    --sky-low: #c4dcef;
    --rule: #8fb0cf;
    --photo-red: #b8311f;
    --photo-red-dark: #8e2418;
    --photo-brass: #a89a78;
    --photo-brass-light: #c9bc98;
    --photo-grass: #6f7a4a;
    --white: #ffffff;
    --icon: #1f4f86;
  }
  * { box-sizing: border-box; margin: 0; padding: 0; }
  html, body { width: 800px; height: 1200px; overflow: hidden; }
  body {
    font-family: "Cabin", Arial, sans-serif;
    color: var(--ink);
    background: linear-gradient(180deg, var(--sky-top) 0%, var(--sky-mid) 55%, var(--sky-low) 100%);
    position: relative;
  }
  .kicker {
    position: absolute; top: 44px; left: 0; width: 800px;
    text-align: center; font-size: 31px; font-weight: 600; letter-spacing: 1px; color: var(--navy);
  }
  .kicker strong { font-weight: 700; font-size: 35px; }
  .headline {
    position: absolute; top: 80px; left: 0; width: 800px;
    text-align: center; font-size: 92px; line-height: 68px; padding-top: 8px; font-weight: 700; color: var(--navy-deep);
    letter-spacing: -0.5px;
  }
  .services {
    position: absolute; top: 244px; left: 0; width: 800px;
    text-align: center; font-size: 23px; font-weight: 600; color: var(--navy);
  }
  .hero-photo {
    position: absolute; top: 292px; left: 86px; width: 628px; height: 332px;
    border-radius: 10px;
    background:
      linear-gradient(180deg, rgba(255,255,255,0) 70%, rgba(255,255,255,0.25) 100%),
      linear-gradient(90deg,
        var(--photo-red-dark) 0%, var(--photo-red) 12%, var(--photo-red) 26%,
        var(--photo-brass) 30%, var(--photo-brass-light) 50%, var(--photo-brass) 70%,
        var(--photo-red) 74%, var(--photo-red) 88%, var(--photo-red-dark) 100%);
    box-shadow: 0 6px 18px rgba(18,51,94,0.18);
  }
  .gallery { position: absolute; top: 645px; left: 51px; width: 701px; height: 182px; }
  .gallery-photo {
    position: absolute; top: 0; height: 182px; border: 4px solid var(--white);
  }
  .gallery-photo.field { left: 0; width: 218px; background: linear-gradient(160deg, var(--photo-grass), var(--photo-brass) 55%, var(--photo-red)); }
  .gallery-photo.spray-a { left: 229px; width: 241px; background: linear-gradient(170deg, #9fb7c8, #b7985a 45%, var(--photo-red) 80%); }
  .gallery-photo.spray-b { left: 481px; width: 220px; background: linear-gradient(170deg, #8fa1a6, #b0914f 45%, var(--photo-red) 80%); }
  .brands-title {
    position: absolute; top: 848px; left: 0; width: 800px;
    display: flex; align-items: center; justify-content: center; gap: 22px;
    font-size: 28px; font-weight: 600; letter-spacing: 1px; color: var(--navy);
  }
  .brands-title::before, .brands-title::after {
    content: ""; width: 106px; height: 2px; background: var(--rule);
  }
  .brand-row {
    position: absolute; top: 898px; left: 40px; width: 718px;
    display: flex; justify-content: space-between; align-items: center;
  }
  .brand { display: flex; align-items: center; gap: 8px; font-size: 20px; font-weight: 700; color: var(--navy); }
  .brand-mark { width: 14px; height: 14px; background: var(--navy); }
  .brand-mark.round { border-radius: 50%; }
  .benefits { position: absolute; top: 963px; left: 80px; list-style: none; }
  .benefits li {
    display: flex; align-items: center; gap: 12px;
    height: 35px; font-size: 25px; font-weight: 500; color: var(--ink);
  }
  .benefits svg { width: 21px; height: 21px; flex: none; }
  .cta {
    position: absolute; top: 1125px; left: 105px; width: 580px; height: 80px;
    background: var(--navy-deep); border-radius: 38px 6px 0 0;
    color: var(--white); text-align: center;
  }
  .cta-drop { position: absolute; left: 22px; top: 24px; width: 30px; height: 40px; }
  .cta-line { margin-top: 6px; font-size: 32px; line-height: 36px; font-weight: 700; padding-left: 34px; }
  .cta-sub { font-size: 27px; line-height: 32px; font-weight: 500; padding-left: 34px; }
</style>
</head>
<body>
  <p class="kicker">YOUR <strong>#1</strong> SOURCE FOR</p>
  <h1 class="headline">Backflow Repair<br>Knowledge</h1>
  <p class="services">Free Technical Assistance &nbsp;•&nbsp; Repair Videos &nbsp;•&nbsp; Step-by-Step Procedures</p>

  <div class="hero-photo" role="img" aria-label="Reduced pressure backflow preventer assembly with red gate valves, brass body and test gauges"></div>

  <div class="gallery">
    <div class="gallery-photo field" role="img" aria-label="Backflow assembly installed outdoors on grass with test gauge attached"></div>
    <div class="gallery-photo spray-a" role="img" aria-label="Brass relief valve discharging water on a red backflow assembly"></div>
    <div class="gallery-photo spray-b" role="img" aria-label="Close view of brass test cocks and relief valve spraying water"></div>
  </div>

  <h2 class="brands-title">BRANDS WE SUPPORT</h2>
  <div class="brand-row">
    <span class="brand"><span class="brand-mark"></span>Aldermoor Valves</span>
    <span class="brand">R.V.T. Flow Parts</span>
    <span class="brand"><span class="brand-mark round"></span>Corvane</span>
    <span class="brand">Heartland Backflow Co.</span>
  </div>

  <ul class="benefits">
    <li><svg viewBox="0 0 20 20"><path fill="var(--icon)" d="M4 2l3 0 1.5 4-2 1.5c1 2.2 2.8 4 5 5l1.5-2 4 1.5 0 3c0 1-1 2-2 2C8 17 3 12 2 4c0-1 1-2 2-2z"/></svg>Call our Toll-Free Technical Support</li>
    <li><svg viewBox="0 0 20 20"><rect x="1" y="3" width="18" height="14" rx="3" fill="var(--icon)"/><path d="M8 7l5 3-5 3z" fill="#fff"/></svg>Access Professional Repair Videos</li>
    <li><svg viewBox="0 0 20 20"><path d="M3 3l14 14M17 3L3 17" stroke="var(--icon)" stroke-width="2.5" stroke-linecap="round"/></svg>Follow Step-by-Step Backflow Repair Guides</li>
    <li><svg viewBox="0 0 20 20"><path d="M10 1l8 4v10l-8 4-8-4V5z" fill="var(--icon)"/><path d="M2 5l8 4 8-4M10 9v10" stroke="#fff" stroke-width="1" fill="none"/></svg>Get the Right Repair Parts Fast</li>
  </ul>

  <div class="cta">
    <svg class="cta-drop" viewBox="0 0 30 40"><path d="M15 2C10 12 4 19 4 26a11 11 0 0 0 22 0C26 19 20 12 15 2z" fill="#7fb6e6"/></svg>
    <p class="cta-line">Visit www.valvemendsupply.com</p>
    <p class="cta-sub">for repair resources</p>
  </div>
</body>
</html>
```